Need simple and modern looking business card with all my information on one side and logo on the other side
Info :
Company name - VELTRIN CONSTRUCTION LLC
Company addres- 418 maple 307th. Dunford hill ny 10583
Email- veltrinllc@pormail.Com
Company phone number 555-318-4096
Cell number- 555-762-0384
Web site - veltrinllc.Com
My name Gerald haverstrom

Target Market(s)

Construction , home improvement, remodeling

Industry/Entity Type

Construction

Contact Information for Business Card

It has to be moder but at the same time simple

Font styles to use
Sans Serif

Colors
0255a3
ffffff
000000
f78f20
b1b1b1
9d9d9d
1b1b1b
33a6d7
ec1f27

Requirements
Must have
• My logo on one side maybe with a some kind of background on the other side all my information
Nice to have
• Some kind of background pictures provided by you .PLEASE HAVE ACCOUNT WITH PIXVALEMOR WILL NOT PAY ANY EXTRA FEES .
Should not have
• Any kind of hamer, nails,screws, helmets itp. Please do not copy the other designs come up with something new.

```html
<!DOCTYPE html>
<html lang="en">
<head>
<meta charset="utf-8">
<title>Veltrin Construction LLC – Business Card</title>
<link rel="stylesheet" href="https://fonts.googleapis.com/css2?family=Comfortaa:wght@400;700&family=Josefin+Sans:wght@400&family=Arimo:wght@400&display=swap">
<style>
  :root {
    --blue-light: #3f84c8;
    --blue: #2466b0;
    --blue-deep: #0255a3;
    --orange: #f78f20;
    --orange-dark: #c96f10;
    --gray: #4e4f52;
    --gray-dark: #3a3b3d;
    --white: #ffffff;
    --ghost: rgba(255, 255, 255, 0.07);
  }
  html, body {
    margin: 0;
    padding: 0;
    width: 1200px;
    height: 720px;
    overflow: hidden;
    background: #ffffff;
  }
  .card {
    position: relative;
    width: 1200px;
    height: 720px;
    overflow: hidden;
    background: radial-gradient(ellipse at 25% 20%, var(--blue-light) 0%, var(--blue) 45%, var(--blue-deep) 100%);
    font-family: "Comfortaa", sans-serif;
    color: var(--white);
  }
  .backdrop-mark {
    position: absolute;
    left: 26px;
    top: 330px;
    margin: 0;
    font-family: "Comfortaa", sans-serif;
    font-weight: 700;
    font-size: 170px;
    letter-spacing: 4px;
    line-height: 1;
    color: var(--ghost);
    white-space: nowrap;
  }
  .brand {
    position: absolute;
    left: 72px;
    top: 190px;
    display: flex;
    align-items: center;
    gap: 16px;
  }
  .brand-square {
    width: 34px;
    height: 34px;
    background: var(--orange);
  }
  .brand-name {
    margin: 0;
    font-family: "Comfortaa", sans-serif;
    font-weight: 700;
    font-size: 64px;
    line-height: 1;
    color: var(--white);
  }
  .company-title {
    position: absolute;
    right: 45px;
    top: 176px;
    margin: 0;
    font-family: "Josefin Sans", sans-serif;
    font-weight: 400;
    font-size: 39px;
    letter-spacing: 1px;
    line-height: 1;
    color: var(--white);
    text-align: right;
    white-space: nowrap;
  }
  .contact {
    position: absolute;
    right: 78px;
    top: 240px;
    margin: 0;
    padding: 0;
    list-style: none;
    text-align: right;
    font-size: 29px;
    line-height: 51px;
    white-space: nowrap;
  }
  .bottom-band {
    position: absolute;
    left: 0;
    top: 0;
    width: 1200px;
    height: 720px;
  }
  .address {
    position: absolute;
    left: 112px;
    top: 650px;
    margin: 0;
    font-family: "Arimo", sans-serif;
    font-size: 56px;
    line-height: 1;
    color: var(--white);
    white-space: nowrap;
  }
</style>
</head>
<body>
  <main class="card">
    <p class="backdrop-mark" aria-hidden="true">VELTRIN</p>

    <div class="brand">
      <span class="brand-square" aria-hidden="true"></span>
      <p class="brand-name">VELTRIN</p>
    </div>

    <h1 class="company-title">VELTRIN CONSTRUCTION LLC</h1>

    <ul class="contact">
      <li class="contact-name">Gerald haverstrom</li>
      <li class="contact-email">Email- veltrinllc@pormail.Com</li>
      <li class="contact-phone">phone number 555-318-4096</li>
      <li class="contact-cell">555-762-0384</li>
      <li class="contact-web">Web site - veltrinllc.Com</li>
    </ul>

    <svg class="bottom-band" viewBox="0 0 1200 720" aria-hidden="true">
      <path d="M0 553 Q600 640 1200 540 L1200 720 L0 720 Z" fill="var(--orange-dark)"/>
      <path d="M0 556 Q600 646 1200 543 L1200 720 L0 720 Z" fill="var(--orange)"/>
      <path d="M0 577 Q600 672 1200 566 L1200 720 L0 720 Z" fill="var(--gray-dark)"/>
      <path d="M0 581 Q600 676 1200 570 L1200 720 L0 720 Z" fill="var(--gray)"/>
    </svg>

    <p class="address">418 maple 307th. Dunford hill ny 10583</p>
  </main>
</body>
</html>
```